Tour agency for FIT and groups need a business card design

We need a business card design for a tour agency company that is based in Perth called" BRISK NO", we aim to provide customise, unique and seamless travel arrangement for FIT and groups. We serve both high profile businessperson, government authorities, business partners, executives and investors. The name card should be more professional looking.
Updates

Project Deadline Extended Reason: Have some changes that needed to make, director will be back to office on Monday, sorry for the inconvenience cause. Added Saturday, May 6, 2017

Target Market(s)

High profile businessperson, government authorities, business partners, executives and investors.

Industry/Entity Type

Tourism

Contact Information for Business Card

Brisk NO
Level 1, 214 Marlowe Avenue, Dunreath NO, 6120
www.briskno.com.au

Font styles to use
Serif

Colors

Designer to choose colors to be used in the design.

Requirements
Must have
• My project must have a company logo
Nice to have
• a more professional and solid yet friendly name card design. We may want to include chinese name in the name card as well. Edge of the card can be filled with gold and we think that transparent name cards are interesting.

```html
<!DOCTYPE html>
<html lang="en">
<head>
<meta charset="utf-8">
<title>Brisk NO – Business Card</title>
<link rel="stylesheet" href="https://fonts.googleapis.com/css2?family=Ubuntu:wght@300;400&display=swap">
<style>
  :root {
    --backdrop: #e4e4e6;
    --card-dark: #1f1d1d;
    --card-light: #ffffff;
    --ink-light: #f2f2f2;
    --ink-dark: #1a1a1a;
    --rule: #8a8a8a;
    --shadow: rgba(0, 0, 0, 0.18);
  }
  * { margin: 0; padding: 0; box-sizing: border-box; }
  html, body {
    width: 1200px; height: 1200px; overflow: hidden;
    background: var(--backdrop);
    font-family: "Ubuntu", sans-serif;
    font-weight: 300;
  }
  .canvas {
    position: relative; width: 1200px; height: 1200px;
    display: flex; flex-direction: column; align-items: center; justify-content: center; gap: 70px;
  }
  .card {
    position: relative; width: 700px; height: 400px;
    box-shadow: 0 10px 30px var(--shadow);
  }
  .card--back { background: var(--card-dark); color: var(--ink-light); }
  .card--front { background: var(--card-light); color: var(--ink-dark);
    display: flex; align-items: center; justify-content: center; }

  .brand { position: absolute; left: 62px; top: 118px; font-size: 46px; letter-spacing: 1px; }
  .person { position: absolute; left: 64px; top: 186px; }
  .person__name { font-size: 22px; letter-spacing: 0.5px; }
  .person__role { font-size: 17px; margin-top: 4px; display: flex; align-items: center; gap: 6px; }
  .person__role svg { width: 12px; height: 16px; }

  .contacts { position: absolute; left: 64px; top: 268px; font-size: 16px; line-height: 26px; }
  .contacts__item { display: flex; align-items: center; gap: 10px; }
  .contacts__item svg { width: 16px; height: 16px; }

  .divider { position: absolute; left: 262px; top: 266px; width: 1px; height: 58px; background: var(--rule); }
  .address { position: absolute; left: 282px; top: 268px; font-size: 17px; line-height: 26px; display: flex; gap: 8px; }
  .address svg { width: 14px; height: 18px; margin-top: 4px; }
  .address-rule { position: absolute; left: 282px; right: 40px; top: 334px; height: 1px; background: var(--rule); }

  .front-mark { display: flex; align-items: center; gap: 16px; }
  .front-mark__dot { width: 40px; height: 40px; border-radius: 50%; background: var(--ink-dark); }
  .front-mark__name { font-size: 52px; letter-spacing: 1px; }
</style>
</head>
<body>
<main class="canvas">
  <section class="card card--back" aria-label="Card back with contact details">
    <div class="brand">BRISK NO</div>
    <div class="person">
      <div class="person__name">ALAN REID</div>
      <div class="person__role">Director |
        <svg viewBox="0 0 12 16" aria-hidden="true"><rect x="1.5" y="0.8" width="9" height="14.4" rx="1.5" fill="none" stroke="currentColor" stroke-width="1.3"/><rect x="3.5" y="3" width="5" height="5" fill="currentColor"/></svg>
        555-014-2288</div>
    </div>
    <div class="contacts">
      <div class="contacts__item">
        <svg viewBox="0 0 16 16" aria-hidden="true"><g fill="none" stroke="currentColor" stroke-width="1.1"><circle cx="8" cy="8" r="6.8"/><ellipse cx="8" cy="8" rx="3" ry="6.8"/><path d="M1.2 8h13.6M2.2 4.5h11.6M2.2 11.5h11.6"/></g></svg>
        www.briskno.com.au</div>
      <div class="contacts__item">
        <svg viewBox="0 0 16 16" aria-hidden="true"><rect x="0.5" y="3" width="15" height="10" fill="currentColor"/><path d="M0.5 3l7.5 6 7.5-6" fill="none" stroke="#1f1d1d" stroke-width="1.2"/></svg>
        alan@briskno.com.au</div>
    </div>
    <div class="divider"></div>
    <div class="address">
      <svg viewBox="0 0 14 18" aria-hidden="true"><path d="M7 17s6-6.5 6-10.5A6 6 0 0 0 1 6.5C1 10.5 7 17 7 17z" fill="none" stroke="currentColor" stroke-width="1.6"/><circle cx="7" cy="6.5" r="2" fill="currentColor"/></svg>
      <span>Level 1, 214 Marlowe Avenue<br>Dunreath NO, 6120</span>
    </div>
    <div class="address-rule"></div>
  </section>

  <section class="card card--front" aria-label="Card front with company name">
    <div class="front-mark">
      <span class="front-mark__dot" aria-hidden="true"></span>
      <span class="front-mark__name">BRISK NO</span>
    </div>
  </section>
</main>
</body>
</html>
```